【 概要 】 都内で7年目のイタリアンレストランです。 コロナ渦でテイクアウト営業に勤しんでおります。 今までスタッフが書いたチラシで頑張ってましたが、メニュー改訂もあり是非プロのお力添えを頂きたく募集致しました。 素敵なデザインを楽しみにしております。 【 依頼内容 】 ・サイズ:A4 片面 ・ページ数:1ページ ・素材の用意(画像・文章等):添付ファイル1枚目がメニューです ・デザイン内容:添付ファイル2枚目がイメージです。料理や人物を参考にお願いします 【 デザインイメージ 】 ・ターゲット層:都心在住の30〜50代男女 ・雰囲気:ナチュラルでおしゃれな雰囲気 ・参考デザイン: お店のイメージ(URL参考)添付ファイル2枚目参照 【 契約金額(税抜) 】 2万円 ※契約金額(税込)からシステム利用料を差し引いた金額が、ワーカーさまの受取金額となります その他ご質問等ありましたら、気軽にお問い合わせください。 ご応募をお待ちしております! |
| https://find.kumoriba.co.jp/amp/s/s.shokunavi-ranpo.jp/tokyo/B2401/B240305/24085917/top_amp/%3Fusqp%3Dxr482KZTMBHZBafV9N3q9-vY6RHxBTB%253D | ||
この度は有難うございます。また細かな修正も早急に対応してくださりありがたかったです。お陰で妥協なくイメージしたデザインに仕上がりました。スキルも高く誠意も伝わりとても感謝致します。また機会がございましたら宜しくお願い致します。
この度は皆様素敵なデザインをありがとうございました!皆様の素敵なデザインに感動し感謝の気持ちでいっぱいでした。コロナ渦で皆様も大変な状況だと思いますが、私も頑張ろうという気持ちになりました。心からありがとうございました。

```html
<!DOCTYPE html>
<html lang="ja">
<head>
<meta charset="utf-8">
<title>TRATTORIA VENTO Take Out Menu</title>
<link rel="stylesheet" href="https://fonts.googleapis.com/css2?family=Noto+Sans+JP:wght@400;500;700&family=Cinzel:wght@600;700&family=Playfair+Display:ital,wght@0,600;1,500&display=swap">
<style>
:root{
  --bg-brown:#3b2e27;
  --bg-stripe:#463830;
  --leaf-green:#2f5a1f;
  --tomato-red:#b3141c;
  --paper:#ffffff;
  --cream:#efe6cf;
  --ink:#2a211c;
  --rule:#c9b9ae;
}
*{margin:0;padding:0;box-sizing:border-box}
html,body{width:848px;height:1200px;overflow:hidden}
body{
  font-family:"Noto Sans JP",sans-serif;color:var(--ink);
  background:repeating-linear-gradient(90deg,var(--bg-brown) 0 6px,var(--bg-stripe) 6px 9px);
  position:relative;
}
.photo{position:absolute;border:4px solid var(--paper)}
.brand{position:absolute;left:0;top:0;width:410px;height:148px;text-align:center;color:var(--paper)}
.brand-small{font-family:"Cinzel",serif;font-size:20px;letter-spacing:5px;margin-top:16px}
.brand-name{font-family:"Cinzel",serif;font-size:68px;font-weight:700;letter-spacing:4px;line-height:1;margin-top:2px}
.intro{position:absolute;left:0;top:150px;width:410px;height:262px;background:var(--leaf-green);color:var(--paper);padding:26px 0 0 28px}
.intro-title{font-family:"Playfair Display",serif;font-size:42px;font-weight:600;line-height:1.1}
.intro-lead{font-size:17px;line-height:1.5;margin-top:14px;font-weight:500}
.intro-phone{display:flex;align-items:center;gap:6px;font-size:26px;font-weight:700;margin-top:10px}
.intro-icons{height:34px;width:140px;margin-top:14px;background:linear-gradient(90deg,#e9e3d4,#cfc6b0);opacity:.55;border-radius:4px}
.chef{position:absolute;left:252px;top:305px;width:140px;height:100px;background:var(--cream);border-radius:4px}
.chef-art{position:absolute;left:40px;top:8px;width:60px;height:38px;background:linear-gradient(#d8ccb0,#c4b391);border-radius:50% 50% 6px 6px}
.chef-note{position:absolute;left:10px;right:10px;bottom:8px;font-size:11px;line-height:1.4;text-align:center;border:1px solid var(--ink);padding:4px;color:var(--ink)}
.menu-card{position:absolute;background:var(--paper);padding:10px 14px 10px 0}
.menu-title{display:flex;align-items:baseline;gap:10px;background:var(--tomato-red);color:var(--paper);font-family:"Cinzel",serif;font-weight:700;font-size:21px;letter-spacing:2px;padding:3px 14px;margin-right:-14px}
.menu-note{font-family:"Noto Sans JP",sans-serif;font-size:11px;letter-spacing:0;font-weight:500;margin-left:auto}
.menu-list{list-style:none;padding:8px 0 0 22px;font-size:15px;line-height:1.55}
.menu-list li{display:flex;justify-content:space-between;gap:8px}
.menu-list small{font-size:10px}
.price{white-space:nowrap;min-width:70px;text-align:right}
</style>
</head>
<body>

<header class="brand">
  <p class="brand-small">TRATTORIA</p>
  <p class="brand-name">VENTO</p>
</header>

<section class="intro">
  <h1 class="intro-title">Take Out Menu</h1>
  <p class="intro-lead">当店のお料理を<br>お持ち帰りしていただけます</p>
  <p class="intro-phone">
    <svg width="26" height="26" viewBox="0 0 24 24" aria-hidden="true"><path fill="#fff" d="M6.6 10.8a15 15 0 0 0 6.6 6.6l2.2-2.2c.3-.3.7-.4 1-.2 1.1.4 2.3.6 3.6.6.6 0 1 .4 1 1V20c0 .6-.4 1-1 1A17 17 0 0 1 3 4c0-.6.4-1 1-1h3.5c.6 0 1 .4 1 1 0 1.3.2 2.5.6 3.6.1.3 0 .7-.2 1z"/></svg>
    03-5550-1482
  </p>
  <div class="intro-icons" role="img" aria-label="料理と食器の小さな線画"></div>
</section>

<aside class="chef">
  <div class="chef-art" role="img" aria-label="シェフのイラスト"></div>
  <p class="chef-note">事前のご予約を<br>お願いいたします</p>
</aside>

<div class="photo" style="left:0;top:425px;width:410px;height:190px;background:linear-gradient(135deg,#e6b870,#b8743a 60%,#7a8a4a)" role="img" aria-label="前菜とキッシュの写真"></div>
<section class="menu-card" style="left:0;top:605px;width:410px;height:282px">
  <h2 class="menu-title">ANTIPASTO</h2>
  <ul class="menu-list">
    <li><span>アンチョビポテト</span><span class="price">¥500</span></li>
    <li><span>ゴルゴンゾーラのキッシュ <small>(2ピース)</small></span><span class="price">¥600</span></li>
    <li><span>ピクルス＆オリーブ</span><span class="price">¥500</span></li>
    <li><span>合鴨のロースト</span><span class="price">¥900</span></li>
    <li><span>いいだこのトマト煮</span><span class="price">¥950</span></li>
    <li><span>ローストビーフ</span><span class="price">¥1,200</span></li>
    <li><span>ローストポーク</span><span class="price">¥900</span></li>
  </ul>
</section>

<div class="photo" style="left:0;top:835px;width:410px;height:130px;background:linear-gradient(135deg,#c9b89a,#8c7a5e 55%,#d9d0c0)" role="img" aria-label="あさりのパスタの写真"></div>
<section class="menu-card" style="left:0;top:955px;width:410px;height:212px">
  <h2 class="menu-title">PASTA <span class="menu-note">※麺は全てリングイネです</span></h2>
  <ul class="menu-list">
    <li><span>はまぐりと大粒あさりのボンゴレビアンコ</span><span class="price">¥1,500</span></li>
    <li><span>わたりがにのトマトクリーム</span><span class="price">¥1,500</span></li>
    <li><span>にんにくとアンチョビのペペロンチーノ</span><span class="price">¥900</span></li>
    <li><span>ゴルゴンゾーラのペンネ</span><span class="price">¥1,300</span></li>
    <li><span>アラビアータのペンネ</span><span class="price">¥1,000</span></li>
  </ul>
</section>

<div class="photo" style="left:425px;top:12px;width:412px;height:170px;background:linear-gradient(90deg,#d9c98a,#e2b45a 50%,#c9652e)" role="img" aria-label="クリーム煮とアヒージョの写真"></div>
<section class="menu-card" style="left:425px;top:175px;width:412px;height:172px">
  <h2 class="menu-title">SPECIALITA</h2>
  <ul class="menu-list" style="line-height:1.45">
    <li><span>天使の海老のクリーム煮</span><span class="price">¥1,500</span></li>
    <li><span>つぶ貝と小海老のエスカルゴバター</span><span class="price">¥900</span></li>
    <li><span>魚介の煮込み雑炊アヒージョ <small>(バゲット付)</small></span><span class="price">¥900</span></li>
    <li><span>ラザニア</span><span class="price">¥1,000</span></li>
    <li><span>バゲット <small>(2ピース)</small></span><span class="price">¥300</span></li>
  </ul>
</section>

<div class="photo" style="left:425px;top:342px;width:412px;height:132px;background:linear-gradient(90deg,#e8c07a,#c97a3a 50%,#e3cf9a)" role="img" aria-label="ピザの写真"></div>
<section class="menu-card" style="left:425px;top:470px;width:412px;height:152px">
  <h2 class="menu-title">PIZZA</h2>
  <ul class="menu-list" style="line-height:1.45">
    <li><span>マルゲリータ</span><span class="price">¥1,500</span></li>
    <li><span>クアトロフォルマッジョ</span><span class="price">¥1,700</span></li>
    <li><span>博多明太子のクリームピザ</span><span class="price">¥1,600</span></li>
    <li><span>ザ・サルシッチャ</span><span class="price">¥1,600</span></li>
  </ul>
</section>

<div class="photo" style="left:425px;top:618px;width:412px;height:85px;background:linear-gradient(90deg,#6f9a3a,#b9c65a 50%,#c0453a)" role="img" aria-label="グリーンサラダの写真"></div>
<section class="menu-card" style="left:425px;top:698px;width:412px;height:180px">
  <h2 class="menu-title">INSALATA <span class="menu-note">※3〜4名様</span></h2>
  <ul class="menu-list">
    <li><span>生ハムのグリーンサラダ</span><span class="price">¥1,000</span></li>
    <li><span>イタリアンだけどフレンチサラダ</span><span class="price">¥1,000</span></li>
    <li><span>VENTOのシーザーサラダ</span><span class="price">¥1,000</span></li>
    <li><span>フレンチサラダS</span><span class="price">¥450</span></li>
  </ul>
</section>

<div class="photo" style="left:425px;top:875px;width:412px;height:108px;background:linear-gradient(90deg,#c8a47a,#6a4a34 55%,#3a2a22)" role="img" aria-label="ティラミスとガトーショコラの写真"></div>
<section class="menu-card" style="left:425px;top:978px;width:412px;height:189px">
  <h2 class="menu-title">DOLCE</h2>
  <ul class="menu-list">
    <li><span>ガトーショコラ</span><span class="price">¥500</span></li>
    <li><span>ティラミス</span><span class="price">¥500</span></li>
  </ul>
</section>

</body>
</html>
```